Gif animated banner ads for Vexaro and Social Media ads for PageLoomly.com

Please make banner ads to promote PageLoomly's new Affiliate Program. PageLoomly is an AI Website Builder that instantly generates beautiful websites for all types of businesses.

I prefer gif animated banners, but I am open to non-animated banners if they look great and you don't offer gifs.

The points to focus on for the content are:
A. Every business needs a website
B. They earn BIG commissions by referring the #1 website builder platform, PageLoomly.com
C. PageLoomly pays 30% recurring commission on every sale
D. Affiliate program is through AllyHarbor, a trusted Affiliate Platform

Obviously, you won't be able to include all that content on each banner, especially since some are fairly small in size. However, please be creative and try to hit the bullet points that will get the viewer's attention.

I need the banner ads made in 26 sizes as follows:
200 × 200
240 × 400
250 × 250
250 × 360
300 × 250
336 × 280
580 × 400
120 × 600
160 × 600
300 × 600
300 × 1050
468 × 60
728 × 90
930 × 180
970 × 90
970 × 250
980 × 120
300 × 50
320 × 50
320 × 100
1200 x 620
1080 x 1080
1200 x 1200
720 x 1280
1280 x 720
640 x 640

I have attached some variations of the PageLoomly logo. Feel free to incorporate it into your banners.

I look forward to seeing your work!

Target Market(s)

Businesses

Industry/Entity Type

Technology, Internet, Artificial Intelligence (AI)

Colors
0054AA
0677BA
7BADD7
CADEEF
E8F1F8

Requirements
Must have
• Must be eye-catching

```html
<!DOCTYPE html>
<html lang="en">
<head>
<meta charset="utf-8">
<title>PageLoomly – Affiliate Banner 1200×232</title>
<link rel="stylesheet" href="https://fonts.googleapis.com/css2?family=Poppins:ital,wght@0,600;0,700;1,800&display=swap">
<style>
  :root {
    --panel-navy: #0c2240;
    --scene-dark: #1b2326;
    --scene-teal: #2f5a5c;
    --scene-glow: #3f8c8a;
    --button-blue: #4bb6ee;
    --text-white: #ffffff;
    --accent-yellow: #f6ea18;
    --mark-blue: #1f9be8;
  }
  * { margin: 0; padding: 0; box-sizing: border-box; }
  html, body {
    width: 1200px;
    height: 232px;
    overflow: hidden;
    background: var(--panel-navy);
  }
  .banner {
    position: relative;
    width: 1200px;
    height: 232px;
    overflow: hidden;
    font-family: "Poppins", sans-serif;
  }
  .banner__scene {
    position: absolute;
    inset: 0 0 0 335px;
    background:
      radial-gradient(ellipse 260px 200px at 300px 110px, rgba(63,140,138,0.55), transparent 70%),
      radial-gradient(ellipse 220px 160px at 760px 60px, rgba(47,90,92,0.5), transparent 70%),
      linear-gradient(100deg, var(--scene-dark) 0%, #24302f 40%, var(--scene-teal) 70%, #1e2a2c 100%);
  }
  .banner__scene::after {
    content: "";
    position: absolute;
    inset: 0;
    background: rgba(10, 14, 16, 0.45);
  }
  .brand-panel {
    position: absolute;
    left: 0;
    top: 0;
    width: 335px;
    height: 232px;
    background: var(--panel-navy);
  }
  .brand {
    position: absolute;
    left: 39px;
    top: 58px;
    display: flex;
    align-items: center;
    gap: 12px;
  }
  .brand__square {
    width: 34px;
    height: 34px;
    border-radius: 4px;
    background: var(--mark-blue);
  }
  .brand__name {
    color: var(--text-white);
    font-weight: 600;
    font-size: 33px;
    line-height: 1;
    letter-spacing: -0.3px;
  }
  .cta {
    position: absolute;
    left: 39px;
    top: 119px;
    width: 255px;
    height: 46px;
    border-radius: 10px;
    background: var(--button-blue);
    color: var(--text-white);
    font-weight: 600;
    font-size: 20px;
    line-height: 46px;
    text-align: center;
    text-decoration: none;
  }
  .headline {
    position: absolute;
    left: 335px;
    right: 0;
    top: 44px;
    text-align: center;
    color: var(--text-white);
    font-weight: 800;
    font-style: italic;
    font-size: 52px;
    line-height: 68px;
    text-transform: uppercase;
    letter-spacing: -0.5px;
  }
  .headline__line { display: block; }
  .headline__accent { color: var(--accent-yellow); }
</style>
</head>
<body>
  <div class="banner">
    <div class="banner__scene" role="img" aria-label="Dark blurred background photo of a glowing teal dollar coin"></div>

    <div class="brand-panel">
      <div class="brand">
        <span class="brand__square"></span>
        <span class="brand__name">PageLoomly</span>
      </div>
      <a class="cta" href="#">Click To Learn More!</a>
    </div>

    <h1 class="headline">
      <span class="headline__line">Almost every <span class="headline__accent">business needs</span></span>
      <span class="headline__line">A <span class="headline__accent">website</span> to build credibility</span>
    </h1>
  </div>
</body>
</html>
```